Label and packaging - Lune de Sable

We are after label and pack design for a product called Lune de Sable. This product is a blend of Pinot Gris and Apple Cider.

Lune de Sable:

The packaging needs to accomplish the following: quickly explain what the product is, establish as a premium price product and grab the eye. The package should also reflect the product innovation.

Quickly Explain What the Product Is:

Lune de Sable is a nice name that could lift the image – but no one will have any idea what the product is by the name. Consider that a consumer will be staring at a shelf, then the bottle for maybe two to three seconds before moving on to another bottle. In those three seconds we need to make certain that they understand that the product is a blend of wine and cider. Lune de Sable will not support this on its own.

Suggestion is to use words like Wine, Cider, Orchard, Vine, Apple, Heirloom, Exotic and make it simple. Perhaps a sticker that says “50% Wine/50% Apple Cider” that sits on the neck of every bottle. They need to quickly ‘get it”. Imagery will assist as well. Consider a hybrid 50/50 image of wine grapes and apples to tell the story.

Establish a Premium Price Point:

The label needs to say high quality in the package and the font. Have fun with the shipper – this is where you can have a field day with imagery and fun buzz words – we love the idea of a busy shipper that tells the story with a clean and smart looking bottle.

Target Market(s)

This is a premium product targeted at females of age 25-45.

Industry/Entity Type

Consumer

Colors
ec1f27
9bcb3c

Requirements
Must have
• Label design on a burgundy bottle with a screw cap, see here for bottle shape: http://www.vexlabottles.co.nz/wine/#/?view=thumbs&segments=41&colors=&capacityMin=187&capacityMax=750&heightMin=171&heightMax=334&labelMin=44&labelMax=168&neckMin=0&neckMax=1000

Packaging design on a 12 x 750ml carton. This sort of thing: https://www.brakunstores.com.au/images/photo06.jpg

Nice to have
• We have attached some examples of a concept we quite like but it's not bright enough.

```html
<!DOCTYPE html>
<html lang="en">
<head>
<meta charset="utf-8">
<title>Lune de Sable – Label Range</title>
<link rel="stylesheet" href="https://fonts.googleapis.com/css2?family=Raleway:wght@400;500&family=Arimo:wght@400&display=swap">
<style>
  :root {
    --page: #ffffff;
    --white-label: #eee8c6;
    --rose-label: #ea9b86;
    --red-label: #3b1520;
    --ink-dark: #3e3a33;
    --cream: #fbf1c6;
    --apple-orange: #ee6a1e;
    --apple-deep: #d9481a;
    --leaf-green: #6a9a3c;
  }
  * { box-sizing: border-box; margin: 0; padding: 0; }
  html, body {
    width: 1194px;
    height: 1200px;
    overflow: hidden;
    background: var(--page);
  }
  .label-range {
    position: relative;
    width: 1194px;
    height: 1200px;
    display: flex;
    justify-content: center;
    align-items: center;
    gap: 60px;
  }
  .label {
    position: relative;
    width: 300px;
    height: 640px;
    border-radius: 6px;
    display: flex;
    flex-direction: column;
    align-items: center;
    padding-top: 190px;
  }
  .label--white { background: var(--white-label); color: var(--ink-dark); }
  .label--rose  { background: var(--rose-label);  color: var(--cream); }
  .label--red   { background: var(--red-label);   color: var(--cream); }

  .apple-mark {
    width: 150px;
    height: 150px;
    border-radius: 50%;
  }
  .label--white .apple-mark {
    background: radial-gradient(circle at 40% 40%, var(--apple-orange) 55%, var(--apple-deep) 100%);
  }
  .label--rose .apple-mark,
  .label--red .apple-mark {
    background: radial-gradient(circle, rgba(251,241,198,0.35) 40%, rgba(251,241,198,0.85) 75%, rgba(251,241,198,0) 100%);
  }

  .vintage {
    font-family: "Arimo", Arial, sans-serif;
    font-size: 12px;
    letter-spacing: 0.5px;
    margin-top: 22px;
    height: 14px;
  }
  .product-name {
    font-family: "Raleway", "Helvetica Neue", sans-serif;
    font-weight: 400;
    font-size: 21px;
    letter-spacing: 1.5px;
    margin-top: 6px;
    white-space: nowrap;
  }
  .product-name .joiner { font-size: 14px; letter-spacing: 1px; }
  .name-rule {
    width: 170px;
    height: 1px;
    background: currentColor;
    opacity: 0.7;
    margin-top: 6px;
  }
  .blend-note {
    font-family: "Arimo", Arial, sans-serif;
    font-size: 13px;
    line-height: 1.2;
    text-align: left;
    width: 170px;
    padding-left: 14px;
    margin-top: 8px;
    opacity: 0.9;
  }
</style>
</head>
<body>
  <main class="label-range">
    <section class="label label--white">
      <div class="apple-mark" role="img" aria-label="Brush-painted orange apple with green leaf and swirl"></div>
      <p class="vintage"></p>
      <h2 class="product-name">LUNE <span class="joiner">de</span> SABLE</h2>
      <div class="name-rule"></div>
      <p class="blend-note">blend of apple cider<br>&amp; pinot gris</p>
    </section>

    <section class="label label--rose">
      <div class="apple-mark" role="img" aria-label="Cream brush-stroke apple outline with swirl"></div>
      <p class="vintage">2011</p>
      <h2 class="product-name">LUNE <span class="joiner">de</span> SABLE</h2>
      <div class="name-rule"></div>
      <p class="blend-note">blend of apple cider<br>&amp; pinot gris</p>
    </section>

    <section class="label label--red">
      <div class="apple-mark" role="img" aria-label="Cream line-drawn apple with swirl and leaf"></div>
      <p class="vintage">2011</p>
      <h2 class="product-name">LUNE <span class="joiner">de</span> SABLE</h2>
      <div class="name-rule"></div>
      <p class="blend-note">blend of apple cider<br>&amp; pinot gris</p>
    </section>
  </main>
</body>
</html>
```